Start-Up Property Development Company Requires Word Press Website Design

A new property development company in Sydney requires a new website.
This version (Version 1) is very simple and will represent one, small aspect of what the company does, which is acquiring properties for redevelopment:

Needed:
- 1 page incorporating copy, logo and illustration.
- Email contact form.
- Contact information.

It will be expanded in the next few months to include another section for marketing homes for sale (Version 2). This section should sit on top of the Version 1 (in the top section of the same scrolling page).

So this initial design must be able to simply incorporate the expansion.

The site design needs to:
- Take up the entire width of the monitor.
- Not be too different from companies corporate look and feel.
- Be simple, functional and elegant.
- Have a long scroll (1 page) with navigation items at the top of the screen simply linking to the corresponding section lower in the page.

Reason: Not happy with the choice of designs. I'm wanting something clean and fresh and not too intensive with graphics.

```html
<!DOCTYPE html>
<html lang="en">
<head>
<meta charset="utf-8">
<title>Norvale Estates</title>
<link href="https://fonts.googleapis.com/css2?family=Lato:wght@400;700;900&display=swap" rel="stylesheet">
<style>
:root{
  --red:#d32a2e;
  --red-dark:#b51f23;
  --ink:#2b2b2b;
  --muted:#666;
  --line:#d9d9d9;
  --field:#f3f3f3;
  --dark:#1f1f1f;
  --footer:#1b1b1b;
  --white:#fff;
}
*{box-sizing:border-box;margin:0;padding:0}
html,body{width:1200px;height:2956px;overflow:hidden}
body{font-family:"Lato",sans-serif;color:var(--ink);background:var(--white);position:relative}
.abs{position:absolute}

/* hero */
.hero{left:0;top:0;width:1200px;height:940px;background:linear-gradient(180deg,#5d646c 0%,#8e959c 35%,#b9bec3 70%,#d8dbde 100%)}
.brand{left:24px;top:14px;width:168px;height:62px;background:var(--white);display:flex;align-items:center;gap:10px;padding:0 12px}
.brand-mark{width:24px;height:24px;background:var(--red)}
.brand-name{font-weight:900;font-size:15px;color:var(--ink);line-height:1.05;text-transform:uppercase}
.nav{right:110px;top:22px;display:flex;gap:4px}
.nav a{color:var(--white);text-decoration:none;font-size:13px;font-weight:700;padding:10px 16px;letter-spacing:.5px}
.nav a.active{background:var(--white);color:var(--ink)}
.hero-title{left:0;top:234px;width:1200px;text-align:center;color:var(--white);font-size:35px;font-weight:900;letter-spacing:.5px;text-shadow:0 2px 6px rgba(0,0,0,.35)}
.search{left:360px;top:296px;width:480px;height:44px;background:rgba(20,20,20,.55);border:1px solid rgba(255,255,255,.5);display:flex;align-items:center;padding:0 16px;color:#eee;font-size:15px;font-style:italic}
.search svg{margin-left:auto}
.dots{left:0;top:464px;width:1200px;display:flex;justify-content:center;gap:10px}
.dots span{width:14px;height:14px;border-radius:50%;border:2px solid var(--white)}
.dots span.on{background:var(--white)}

/* property search panel */
.finder{left:140px;top:540px;width:920px;height:360px;background:var(--white);box-shadow:0 4px 18px rgba(0,0,0,.2)}
.tabs{height:44px;background:var(--red);display:flex;align-items:center}
.tabs span{color:var(--white);font-weight:700;font-size:14px;padding:0 28px;height:44px;line-height:44px}
.tabs span.on{background:var(--red-dark)}
.tabs .advanced{margin-left:auto;margin-right:10px;background:#e4e4e4;color:var(--ink);font-size:12px;height:28px;line-height:28px;padding:0 18px}
.fields{padding:18px 20px 0;display:grid;grid-template-columns:300px 300px 1fr;column-gap:20px;row-gap:14px}
.field label{display:block;font-size:13px;color:var(--muted);margin-bottom:6px}
.select{height:38px;border:1px solid var(--line);background:var(--field);position:relative}
.select:after{content:"";position:absolute;right:0;top:0;width:34px;height:36px;background:#ddd}
.select:before{content:"";position:absolute;right:12px;top:15px;border:5px solid transparent;border-top-color:#777;z-index:1}
.range{height:38px;position:relative}
.range .bar{position:absolute;left:0;right:0;top:16px;height:6px;background:#e0e0e0}
.range .fill{position:absolute;left:0;width:70%;top:16px;height:6px;background:var(--red)}
.range .vals{position:absolute;left:0;right:0;top:26px;display:flex;justify-content:space-between;font-size:12px;color:var(--muted)}
.range .boxes{position:absolute;right:0;top:-26px;display:flex;gap:6px}
.range .boxes i{width:56px;height:18px;background:#ddd;display:block}
.submit-query{left:310px;top:272px;width:300px;height:54px;background:var(--red);color:var(--white);font-weight:700;font-size:16px;text-align:center;line-height:54px;letter-spacing:.5px}

/* how section */
.how-title{left:0;top:1002px;width:1200px;text-align:center;color:var(--red);font-size:28px;font-weight:900}
.how-copy{left:150px;top:1052px;width:900px;text-align:center;font-size:14px;line-height:22px;color:var(--muted)}
.step{top:1196px;width:280px;text-align:center}
.step .ico{width:92px;height:92px;border-radius:50%;background:var(--red);margin:0 auto;display:flex;align-items:center;justify-content:center}
.step h3{margin-top:22px;font-size:17px;font-weight:900;line-height:24px;text-transform:uppercase}
.step-arrow{top:1230px}

/* what we done */
.band{left:0;top:1420px;width:1200px;height:60px;background:var(--red);color:var(--white);text-align:center;font-size:28px;font-weight:900;line-height:60px}
.feature-photo{left:0;top:1480px;width:712px;height:262px;background:linear-gradient(160deg,#1c2a44 0%,#38465e 45%,#a27d4e 80%,#d7a766 100%)}
.custom{left:740px;top:1500px;width:440px}
.custom h3{font-size:21px;font-weight:900}
.custom .arrows{position:absolute;right:0;top:2px;display:flex;gap:8px}
.custom .arrows span{width:24px;height:24px;border-radius:50%;border:2px solid var(--ink);display:flex;align-items:center;justify-content:center}
.custom p{margin-top:10px;font-size:13px;line-height:19px;color:var(--muted)}
.thumbs{margin-top:14px;display:flex;gap:12px}
.thumb{width:138px}
.thumb .pic{height:76px;background:linear-gradient(150deg,#7ea6c9,#6f8c5c 60%,#cfc6b0)}
.thumb span{display:block;margin-top:6px;font-size:13px;font-weight:700;text-align:center;line-height:17px}

/* video */
.video{left:0;top:1742px;width:1200px;height:478px;background:linear-gradient(180deg,#3a2c25 0%,#2a2220 50%,#4a3a30 100%)}
.video h2{position:absolute;left:0;top:48px;width:1200px;text-align:center;color:var(--white);font-size:32px;font-weight:900}
.video p{position:absolute;left:250px;top:98px;width:700px;text-align:center;color:#ddd;font-size:14px;line-height:21px}
.social{position:absolute;left:0;top:164px;width:1200px;display:flex;justify-content:center;gap:14px}
.social span{width:30px;height:30px;border-radius:50%;background:var(--white)}
.play{position:absolute;left:558px;top:270px;width:84px;height:84px;border-radius:50%;border:4px solid var(--white);display:flex;align-items:center;justify-content:center}

/* info columns */
.col{top:2256px;width:290px}
.col h4{color:var(--red);font-size:22px;font-weight:900;padding-bottom:8px;border-bottom:1px solid var(--line)}
.quote{margin-top:16px;border:1px solid var(--line);padding:14px;font-size:12px;line-height:18px;color:var(--muted)}
.person{margin:20px auto 0;width:64px;height:64px;border-radius:50%;background:#c9c3bb;border:3px solid var(--red)}
.person-name{text-align:center;color:var(--red);font-size:12px;margin-top:8px;font-weight:700}
.news{margin-top:16px}
.news li{list-style:none;font-size:12px;line-height:17px;color:var(--muted);margin-bottom:14px;padding-left:14px;position:relative}
.news li:before{content:"";position:absolute;left:0;top:5px;width:6px;height:6px;background:var(--red)}
.news li b{display:block;color:var(--red);font-weight:700;margin-top:2px}
.form{margin-top:16px}
.form .in{height:34px;border:1px solid var(--line);margin-bottom:10px;font-size:12px;color:var(--muted);padding:9px 10px}
.form .in.msg{height:90px}
.form .btn{width:96px;height:34px;background:var(--red);color:var(--white);font-weight:700;font-size:13px;text-align:center;line-height:34px}

/* footer */
.footer{left:0;top:2640px;width:1200px;height:316px;background:var(--footer);color:#ccc;border-top:6px solid var(--red)}
.footer h5{font-size:15px;color:var(--white);font-weight:700;margin-bottom:14px}
.fcol{position:absolute;top:36px}
.links li{list-style:none;font-size:13px;line-height:26px}
.map{width:150px;height:82px;background:linear-gradient(135deg,#d8d4c8,#bfcbb5);margin-bottom:12px}
.contact-line{font-size:13px;line-height:24px;display:flex;align-items:center;gap:8px}
.fcol p{font-size:12px;line-height:18px;width:220px}
.sub-in{width:220px;height:30px;background:#fff;margin-top:12px}
.sub-btn{width:110px;height:30px;background:var(--red);color:#fff;font-size:12px;font-weight:700;text-align:center;line-height:30px;margin-top:10px}
.fbrand{display:flex;align-items:center;gap:10px;color:var(--white);font-weight:900;font-size:22px;text-transform:uppercase}
.fbrand i{width:30px;height:30px;background:var(--white);display:block}
.fsocial{display:flex;gap:8px;margin-top:24px}
.fsocial span{width:28px;height:28px;background:#3a5a9a}
.copy{font-size:12px;margin-top:14px}
</style>
</head>
<body>

<header class="hero abs" role="img" aria-label="Modern multi-storey glass apartment building photographed from street level"></header>
<div class="brand abs"><span class="brand-mark"></span><span class="brand-name">Norvale<br>Estates</span></div>
<nav class="nav abs">
  <a class="active">HOME</a><a>ABOUT US</a><a>SERVICES</a><a>PROPERTY</a><a>GALLERY</a><a>CONTACT US</a>
</nav>
<h1 class="hero-title abs">WE BRING YOU NEW AND OLD PROPERTIES OF AUSTRALIA</h1>
<div class="search abs">Find your property with the search engine
  <svg width="20" height="20" viewBox="0 0 20 20"><circle cx="8" cy="8" r="6" fill="none" stroke="#fff" stroke-width="2"/><line x1="12.5" y1="12.5" x2="18" y2="18" stroke="#fff" stroke-width="2"/></svg>
</div>
<div class="dots abs"><span class="on"></span><span></span><span></span></div>

<section class="finder abs">
  <div class="tabs">
    <span class="on">ALL PROPERTIES</span><span>RESIDENTIAL</span><span>COMMERCIAL</span><span>CUSTOME</span>
    <span class="advanced">ADVANCED SEARCH</span>
  </div>
  <div class="fields">
    <div class="field"><label>Property type</label><div class="select"></div></div>
    <div class="field"><label>Location</label><div class="select"></div></div>
    <div class="field"><label>Price Range</label><div class="range"><div class="boxes"><i></i><i></i></div><div class="bar"></div><div class="fill"></div><div class="vals"><span>$10,000</span><span>$50,000</span></div></div></div>
    <div class="field"><label>Bedroom</label><div class="select"></div></div>
    <div class="field"><label>Baths</label><div class="select"></div></div>
    <div class="field"><label>Area Sqft</label><div class="range"><div class="bar"></div><div class="fill" style="width:55%"></div><div class="vals"><span>$10,000</span><span>$30,000</span></div></div></div>
  </div>
  <div class="submit-query abs">SUBMIT YOUR QUERIES</div>
</section>

<h2 class="how-title abs">We Make Yout Life Easy. Heres How.</h2>
<p class="how-copy abs">Lorem ipsum dolor sit amet, consectetuer adipiscing elit, sed diam nonummy nibh euismod tincidunt ut laoreet dolore magna aliquam erat volutpat. Ut wisi enim ad minim veniam, quis nostrud exerci tation ullamcorper suscipit lobortis nisl ut aliquip ex ea commodo consequat. Duis autem vel eum iriure dolor in hendrerit in vulputate velit esse molestie consequat, vel illum dolore eu feugiat nulla facilisis at vero eros et accumsan et iusto odio dignissim qui blandit praesent.</p>

<div class="step abs" style="left:160px">
  <div class="ico"><svg width="44" height="44" viewBox="0 0 44 44"><circle cx="22" cy="22" r="17" fill="none" stroke="#fff" stroke-width="3"/><path d="M22 10 a8 8 0 0 1 8 8 c0 6 -8 14 -8 14 s-8 -8 -8 -14 a8 8 0 0 1 8 -8z" fill="#fff"/></svg></div>
  <h3>Hottest<br>Property Locations</h3>
</div>
<svg class="step-arrow abs" style="left:420px" width="80" height="20" viewBox="0 0 80 20"><line x1="0" y1="10" x2="70" y2="10" stroke="#bbb" stroke-width="2"/><path d="M68 4 L78 10 L68 16" fill="none" stroke="#bbb" stroke-width="2"/></svg>
<div class="step abs" style="left:460px">
  <div class="ico"><svg width="44" height="44" viewBox="0 0 44 44"><circle cx="22" cy="15" r="7" fill="#fff"/><path d="M9 36 c0-9 6-13 13-13 s13 4 13 13z" fill="#fff"/></svg></div>
  <h3>Knowledgable<br>Property Agents</h3>
</div>
<svg class="step-arrow abs" style="left:720px" width="80" height="20" viewBox="0 0 80 20"><line x1="0" y1="10" x2="70" y2="10" stroke="#bbb" stroke-width="2"/><path d="M68 4 L78 10 L68 16" fill="none" stroke="#bbb" stroke-width="2"/></svg>
<div class="step abs" style="left:760px">
  <div class="ico"><svg width="48" height="44" viewBox="0 0 48 44"><circle cx="24" cy="12" r="6" fill="#fff"/><circle cx="10" cy="16" r="5" fill="#fff"/><circle cx="38" cy="16" r="5" fill="#fff"/><path d="M14 36 c0-8 4-12 10-12 s10 4 10 12z M2 34 c0-6 3-9 8-9 s6 2 6 4z M46 34 c0-6 -3-9 -8-9 s-6 2 -6 4z" fill="#fff"/></svg></div>
  <h3>Expert<br>Architects</h3>
</div>

<div class="band abs">What We Done</div>
<div class="feature-photo abs" role="img" aria-label="Luxury home with lit pool and terrace at dusk"></div>
<div class="custom abs">
  <h3>Custom Homes</h3>
  <div class="arrows">
    <span><svg width="10" height="10" viewBox="0 0 10 10"><path d="M7 1 L3 5 L7 9" fill="none" stroke="#2b2b2b" stroke-width="2"/></svg></span>
    <span><svg width="10" height="10" viewBox="0 0 10 10"><path d="M3 1 L7 5 L3 9" fill="none" stroke="#2b2b2b" stroke-width="2"/></svg></span>
  </div>
  <p>Lorem ipsum dolor sit amet, consectetuer adipiscing elit, sed diam nonummy nibh euismod tincidunt ut laoreet dolore magna aliquam erat volutpat. Ut wisi enim ad minim veniam, quis nostrud exerci tation ullamcorper.</p>
  <div class="thumbs">
    <div class="thumb"><div class="pic" role="img" aria-label="Modern house exterior"></div><span>Lorem ipsum<br>dolor</span></div>
    <div class="thumb"><div class="pic" role="img" aria-label="Contemporary home with garden"></div><span>Lorem ipsum<br>dolor</span></div>
    <div class="thumb"><div class="pic" role="img" aria-label="Residential building facade"></div><span>Lorem ipsum<br>dolor</span></div>
  </div>
</div>

<section class="video abs" role="img" aria-label="Warm-toned modern kitchen and living interior">
  <h2>Project Gallery Video</h2>
  <p>Lorem ipsum dolor sit amet, consectetuer adipiscing elit, sed diam nonummy nibh euismod tincidunt ut laoreet dolore magna aliquam erat volutpat. Ut wisi enim ad minim veniam.</p>
  <div class="social"><span></span><span></span><span></span><span></span><span></span><span></span><span></span></div>
  <div class="play"><svg width="30" height="34" viewBox="0 0 30 34"><path d="M4 2 L28 17 L4 32z" fill="#fff"/></svg></div>
</section>

<div class="col abs" style="left:130px">
  <h4>Testimonials</h4>
  <div class="quote">Lorem ipsum dolor sit amet, consectetuer adipiscing elit, sed diam nonummy nibh euismod tincidunt ut laoreet dolore magna aliquam erat volutpat. Lorem ipsum dolor sit amet, consectetuer adipiscing elit, sed diam nonummy nibh euismod tincidunt.</div>
  <div class="person" role="img" aria-label="Client portrait"></div>
  <div class="person-name">Ms. Clara Wendell</div>
</div>

<div class="col abs" style="left:460px">
  <h4>Latest News</h4>
  <ul class="news">
    <li>Lorem ipsum dolor sit amet consectetuer adipiscing elit sed diam nonummy nibh euismod tincidunt.<b>05 Dec 2014</b></li>
    <li>Lorem ipsum dolor sit amet consectetuer adipiscing elit sed diam nonummy nibh euismod tincidunt.<b>05 Dec 2014</b></li>
    <li>Lorem ipsum dolor sit amet consectetuer adipiscing elit sed diam nonummy nibh euismod tincidunt.<b>05 Dec 2014</b></li>
  </ul>
</div>

<div class="col abs" style="left:790px">
  <h4>Get Contact With You</h4>
  <div class="form">
    <div class="in">Name*</div>
    <div class="in">Email*</div>
    <div class="in">Phone*</div>
    <div class="in msg">Message*</div>
    <div class="btn">SUBMIT</div>
  </div>
</div>

<footer class="footer abs">
  <div class="fcol" style="left:130px">
    <h5>Quick Links</h5>
    <ul class="links"><li>Home</li><li>About Us</li><li>Property</li><li>Services</li><li>Project</li><li>Media Centre</li><li>Contact Us</li></ul>
  </div>
  <div class="fcol" style="left:330px">
    <h5>Contact Information</h5>
    <div class="map" role="img" aria-label="Office location map"></div>
    <div class="contact-line"><svg width="14" height="14" viewBox="0 0 14 14"><path d="M3 1 L5 1 L6 4 L4.5 5 a7 7 0 0 0 4.5 4.5 L10 8 L13 9 L13 11 a2 2 0 0 1 -2 2 A10 10 0 0 1 1 3 a2 2 0 0 1 2 -2z" fill="#d32a2e"/></svg>02 5550 1482</div>
    <div class="contact-line"><svg width="14" height="14" viewBox="0 0 14 14"><rect x="1" y="3" width="12" height="8" fill="none" stroke="#d32a2e" stroke-width="1.5"/><path d="M1 3 L7 8 L13 3" fill="none" stroke="#d32a2e" stroke-width="1.5"/></svg>hello@norvaleestates.com</div>
  </div>
  <div class="fcol" style="left:600px">
    <h5>Sign Up For Newsletter</h5>
    <p>Get Valuable Tips and News from Norvale Estates. Sign up to our Monthly Newsletter today!</p>
    <div class="sub-in"></div>
    <div class="sub-btn">SUBSCRIBE</div>
  </div>
  <div class="fcol" style="left:890px">
    <div class="fbrand"><i></i>Norvale Estates</div>
    <div class="fsocial"><span></span><span></span><span></span><span></span><span></span></div>
    <div class="copy">© Copyright 2014 Norvale Estates<br>All Right Reserved.</div>
  </div>
</footer>

</body>
</html>
```